Business Card Design

We sell fish products to corporate food companies who then turn these products into final food products for consumers

Industry/Entity Type

Business

Contact Information for Business Card

I need a corporate business card template for a fish products business. We would like it be professional for use in dealing with multi national companies. This company business card template will be used by multiple employees so the following fields must be open to edit (Name, Phone Number and Email address)

```html
<!DOCTYPE html>
<html lang="en">
<head>
<meta charset="utf-8">
<title>Tidewater Seafoods – Business Cards</title>
<link rel="stylesheet" href="https://fonts.googleapis.com/css2?family=PT+Sans:wght@400;700&display=swap">
<style>
  :root {
    --page-bg: #eceef1;
    --brand-blue: #0b63b8;
    --brand-blue-deep: #0a55a3;
    --brand-blue-light: #1b80d4;
    --brand-navy: #0d4a93;
    --brand-green: #5cc28a;
    --brand-teal: #1aa9d6;
    --card-white: #ffffff;
    --swirl-grey: #e6e7e9;
    --divider: #8fb4dd;
  }
  * { box-sizing: border-box; margin: 0; padding: 0; }
  html, body { width: 1200px; height: 784px; overflow: hidden; }
  body {
    background: var(--page-bg);
    font-family: "PT Sans", Arial, sans-serif;
    position: relative;
  }
  .card {
    position: absolute;
    width: 560px;
    height: 320px;
    border-radius: 4px;
    overflow: hidden;
    box-shadow: 0 6px 18px rgba(0,0,0,0.18);
  }

  /* Front */
  .card-front {
    left: 50px;
    top: 70px;
    background: linear-gradient(160deg, var(--brand-blue-light) 0%, var(--brand-blue) 55%, var(--brand-blue-deep) 100%);
  }
  .card-front .wave-decoration {
    position: absolute;
    left: -60px;
    top: 40px;
    width: 300px;
    height: 300px;
    border-radius: 50%;
    background: radial-gradient(circle, rgba(255,255,255,0.08) 0%, rgba(255,255,255,0) 70%);
  }
  .card-front .brand {
    position: absolute;
    left: 0; right: 0;
    top: 128px;
    text-align: center;
    color: var(--card-white);
    font-weight: 700;
    font-size: 40px;
    letter-spacing: 1px;
  }
  .brand-mark {
    display: inline-block;
    width: 18px; height: 18px;
    border-radius: 50%;
    background: currentColor;
    margin-right: 12px;
    vertical-align: 4px;
  }

  /* Back */
  .card-back {
    left: 590px;
    top: 394px;
    background: var(--card-white);
  }
  .card-back .wave-decoration {
    position: absolute;
    left: 0; top: 0;
    width: 230px; height: 200px;
    background: radial-gradient(ellipse at 30% 60%, var(--swirl-grey) 0%, rgba(230,231,233,0) 72%);
  }
  .card-back .brand {
    position: absolute;
    left: 200px; right: 20px;
    top: 78px;
    text-align: center;
    color: var(--brand-navy);
    font-weight: 700;
    font-size: 32px;
    letter-spacing: 0.5px;
  }
  .card-back .brand .brand-mark { width: 14px; height: 14px; vertical-align: 3px; margin-right: 10px; }
  .accent-stripes {
    position: absolute;
    left: 0; top: 176px;
    width: 100%; height: 10px;
  }
  .accent-stripes .stripe-green { height: 5px; background: var(--brand-green); }
  .accent-stripes .stripe-teal { height: 5px; background: var(--brand-teal); }
  .info-band {
    position: absolute;
    left: 0; top: 186px;
    width: 100%; height: 134px;
    background: linear-gradient(180deg, var(--brand-blue) 0%, var(--brand-blue-deep) 100%);
  }
  .person {
    position: absolute;
    right: 300px;
    top: 30px;
    text-align: right;
  }
  .person-name {
    color: var(--brand-green);
    font-size: 27px;
    line-height: 1.1;
  }
  .person-title {
    color: var(--card-white);
    font-size: 13px;
  }
  .band-divider {
    position: absolute;
    left: 278px;
    top: 18px;
    width: 1px;
    height: 98px;
    background: var(--divider);
  }
  .contact-list {
    position: absolute;
    left: 292px;
    top: 18px;
    list-style: none;
    color: var(--card-white);
    font-size: 13px;
    line-height: 18px;
  }
  .contact-list li { display: flex; align-items: flex-start; gap: 6px; }
  .contact-list svg { width: 12px; height: 12px; margin-top: 3px; flex: none; fill: var(--brand-green); }
  .contact-list .address-cont { padding-left: 18px; }
</style>
</head>
<body>

  <section class="card card-front" aria-label="Business card front">
    <div class="wave-decoration" role="img" aria-label="Faint wave and fish brand motif"></div>
    <div class="brand"><span class="brand-mark"></span>TIDEWATER SEAFOODS</div>
  </section>

  <section class="card card-back" aria-label="Business card back">
    <div class="wave-decoration" role="img" aria-label="Faint wave and fish brand motif"></div>
    <div class="brand"><span class="brand-mark"></span>TIDEWATER SEAFOODS</div>
    <div class="accent-stripes">
      <div class="stripe-green"></div>
      <div class="stripe-teal"></div>
    </div>
    <div class="info-band">
      <div class="person">
        <div class="person-name">Daniel Marsh</div>
        <div class="person-title">manager</div>
      </div>
      <div class="band-divider"></div>
      <ul class="contact-list">
        <li>
          <svg viewBox="0 0 24 24" aria-hidden="true"><path d="M6.6 10.8a15 15 0 0 0 6.6 6.6l2.2-2.2c.3-.3.7-.4 1-.2 1.1.4 2.3.6 3.6.6.6 0 1 .4 1 1V20c0 .6-.4 1-1 1A17 17 0 0 1 3 4c0-.6.4-1 1-1h3.5c.6 0 1 .4 1 1 0 1.3.2 2.5.6 3.6.1.3 0 .7-.2 1z"/></svg>
          <span>0412555019</span>
        </li>
        <li>
          <svg viewBox="0 0 24 24" aria-hidden="true"><path d="M2 5h20v14H2zm2 2v.5l8 5 8-5V7l-8 5z"/></svg>
          <span>daniel@tidewaterseafoods.com</span>
        </li>
        <li>
          <svg viewBox="0 0 24 24" aria-hidden="true"><path d="M12 2a10 10 0 1 0 0 20 10 10 0 0 0 0-20zm0 2c1 0 2.3 2 2.8 5H9.2C9.7 6 11 4 12 4zm-7.7 7h3.8a19 19 0 0 0 0 2H4.3a8 8 0 0 1 0-2zm5 0h5.4a17 17 0 0 1 0 2H9.3a17 17 0 0 1 0-2zm6.6 0h3.8a8 8 0 0 1 0 2h-3.8a19 19 0 0 0 0-2zM9.2 15h5.6c-.5 3-1.8 5-2.8 5s-2.3-2-2.8-5z"/></svg>
          <span>www.tidewaterseafoods.com</span>
        </li>
        <li>
          <svg viewBox="0 0 24 24" aria-hidden="true"><path d="M12 3 2 12h3v9h5v-6h4v6h5v-9h3z"/></svg>
          <span>Unit 12,Harbour Point</span>
        </li>
        <li class="address-cont"><span>Business Hub,Lakeport, CO</span></li>
      </ul>
    </div>
  </section>

</body>
</html>
```